Zielgruppe
Hausarztpraxis Dr. Wildhagen
Patientenbetreuung / Junge Patienten
Aufgabenstellung
Bitte Mit dem Praxis Logo. Gern auch ein Foto aus der Praxis. In den Farben der Praxis Weiß-Magenta-Grau
Es soll kein Newsletter an sich werden, sondern eine Email die die Patienten nach Ihrem Besuch in der Praxis bekommen. Dort soll dann die Suchflixseite verlinkt sein mit einem Button zum bewerten!

```html
<!DOCTYPE html>
<html lang="de">
<head>
<meta charset="utf-8">
<title>Hausarztpraxis Dr. Wildhagen – Bewertung</title>
<link rel="stylesheet" href="https://fonts.googleapis.com/css2?family=Open+Sans:wght@400;600&display=swap">
<style>
  :root {
    --magenta: #c2185b;
    --magenta-soft: rgba(196, 30, 92, 0.82);
    --pink-band: #ef6a9e;
    --grey-text: #5f5f5f;
    --grey-logo: #5a5d60;
    --white: #ffffff;
  }
  * { margin: 0; padding: 0; box-sizing: border-box; }
  html, body { width: 1200px; height: 1139px; overflow: hidden; background: var(--white); }
  body { position: relative; font-family: "Open Sans", sans-serif; color: var(--grey-text); }

  .brand { position: absolute; top: 25px; left: 0; width: 1200px; text-align: center; }
  .brand-mark { display: block; margin: 0 auto; }
  .brand-name { margin-top: 12px; font-size: 17px; font-weight: 600; color: var(--magenta); letter-spacing: 0.5px; line-height: 1.35; }

  .hero-photo { position: absolute; top: 182px; left: 0; width: 1200px; height: 336px;
    background: linear-gradient(90deg, #ecebea 0%, #f4f3f2 40%, #b9aa92 62%, #d6d3cf 78%, #bdbbb9 100%); }

  .hero-pill { position: absolute; top: 431px; left: 260px; width: 680px; height: 151px;
    border-radius: 76px; background: var(--magenta-soft); color: var(--white); text-align: center; }
  .hero-title { position: absolute; top: 32px; width: 100%; font-size: 35px; font-weight: 400; line-height: 1.2; }
  .hero-sub { position: absolute; top: 85px; width: 100%; font-size: 16px; }

  .message { position: absolute; left: 0; width: 1200px; text-align: center; font-size: 15px; line-height: 20px; }
  .greeting { top: 641px; }
  .question { top: 681px; }
  .request { top: 721px; }
  .cta-hint { top: 801px; }
  .thanks { top: 921px; }
  .phone-line { top: 981px; }
  .closing { top: 1021px; }
  .phone { color: var(--magenta); font-weight: 600; }

  .review-button { position: absolute; top: 851px; left: 260px; width: 680px; height: 41px;
    border-radius: 21px; background: var(--magenta); display: flex; align-items: center; justify-content: center; }
  .review-button a { color: var(--white); font-size: 13.5px; text-decoration: underline; }

  .footer-accent { position: absolute; top: 1095px; left: 0; width: 1200px; height: 12px; background: var(--pink-band); }
  .footer { position: absolute; top: 1107px; left: 0; width: 1200px; height: 32px; background: var(--magenta);
    color: var(--white); font-size: 14px; text-align: center; line-height: 32px; }
</style>
</head>
<body>
  <header class="brand">
    <svg class="brand-mark" width="62" height="62" viewBox="0 0 62 62" aria-hidden="true">
      <circle cx="31" cy="31" r="29" fill="none" stroke="var(--magenta)" stroke-width="3"/>
    </svg>
    <p class="brand-name">Hausarztpraxis<br>Dr. med. Henrike Wildhagen</p>
  </header>

  <div class="hero-photo" role="img" aria-label="Foto des hellen Wartebereichs der Praxis mit weißen Schalenstühlen, Bambusstäben und grauen Sesseln"></div>

  <section class="hero-pill">
    <h1 class="hero-title">Ihre Meinung ist uns wichtig.</h1>
    <p class="hero-sub">Nehmen Sie sich kurz zeit und bewerten Sie uns auf Suchflix.</p>
  </section>

  <p class="message greeting">Hallo Frau/Herr....,</p>
  <p class="message question">wie war Ihre Erfahrung bei Dr. Med. Henrike Wildhagen?</p>
  <p class="message request">Wir versuchen ständig, uns zu verbessern und freuen uns, wenn du uns dein Feedback mitteilen<br>könntest. Es wäre toll, wenn du dir kurz die Zeit nimmst, eine Bewertung bei Suchflix zu schreiben,<br>denn damit hilfst du uns und auch anderen Kunden uns zu finden.</p>
  <p class="message cta-hint">Um Ihre Bewertung zu schreiben und abzuschicken, genügt ein Klick!</p>

  <div class="review-button"><a href="#">Jetzt Hausarztpraxis Dr.Med.Henrike Wildhagen bewerten</a></div>

  <p class="message thanks">Vielen Dank im Voraus für deine Bewertung! Bei Fragen oder falls Sie uns erneut besuchen möchtest,<br>stehen wir dir jederzeit gerne zur Verfügung!</p>
  <p class="message phone-line">Rufen Sie uns an unter der <span class="phone">07000- 12 34</span>.</p>
  <p class="message closing">Viele Grüße,<br>Ihre Hausarztpraxis</p>

  <div class="footer-accent"></div>
  <footer class="footer">Impressum &nbsp;I Datenschutz I Unsere Praxis I Kontakt</footer>
</body>
</html>
```